For Sale Poster Design

We need a beautiful and tropical looking FOR SALE poster for our speed boat.

Poster format need to be 297x420mm / 300dpi
PSD with all layers.

The photos from the boat can be downloaded here: www.dorpukan.nl/photos.zip

Target Market(s)

Tourists, expats

Requirements
Must have
• The poster need to have the following text:

Speed Boat Sale

This beautiful full glass fiber speedboat (location Lombok, Indonesia) is perfect for tropical conditions: island transfer, diving, wake boarding, fishing, private charters and leisure activities.

The newly bought 2x 200 HP KELTOR 4 Stroke (2013) will give you an enormous power on the water with maximum speed of 40 Knot / 74 Km/hour. This will bring you from Lombok to Bali in just 50 minutes and only few minutes long from the famous tropical Gili islands.

The speedboat also has the comfort of a small cabin with skylight, sun controlled ventilation system, a small bed, a toilet and a fridge. There are 16 seats in the open section of the boat. The boat is equipped with modern brand-new GPS, Sonar and an FM / AM Radio system.

This speedboat was built in 2011 and is meticulously maintained to the highest standard. It comes with a captain and boatman.

Specs:
Overall length: 11 Meter 36 feet.
Built year: 2011, Bali
Engines: 2x 200 HP KELTOR 4 Stroke (Bought 2013)
Capacity: Max. 16 People (Incl. Crew)
Max speed: 40 Knot / 74 Km/hour
GPS / Sonar: Mostrel QX-52RB
Tankage: 300 Liter
Lighting: LED / Halogen

Price 99.000 USD
Nice to have
• Big FOR SALE banner on the poster

```html
<!DOCTYPE html>
<html lang="en">
<head>
<meta charset="utf-8">
<title>Speed Boat For Sale Poster</title>
<link href="https://fonts.googleapis.com/css2?family=Montserrat:wght@700;800&family=Questrial&family=Oswald:wght@500;700&display=swap" rel="stylesheet">
<style>
  :root {
    --stage: #141414;
    --sky-top: #a8b2f6;
    --sky-mid: #9fc4f6;
    --cyan: #4fe6ef;
    --band-light: rgba(190, 240, 255, 0.55);
    --ink: #1d1d2a;
    --red: #e8141c;
    --red-dark: #9c0b10;
    --frame: #6a3c1d;
    --cabin: #d9d4c6;
    --cabin-light: #eeece6;
    --sea: #2fc7c9;
    --sand: #e9dcbc;
    --leaf: #3f7a2a;
  }
  * { margin: 0; padding: 0; box-sizing: border-box; }
  html, body { width: 789px; height: 1200px; overflow: hidden; }
  body { background: var(--stage); position: relative; }

  .poster {
    position: absolute; left: 0; top: 42px;
    width: 789px; height: 1116px; overflow: hidden;
    background: linear-gradient(160deg, var(--sky-top) 0%, var(--sky-mid) 45%, #86d6f4 70%, var(--cyan) 100%);
    font-family: "Questrial", sans-serif; color: var(--ink);
  }
  .light-band { position: absolute; inset: 0; }

  .headline {
    position: absolute; top: 18px; left: 0; width: 100%; text-align: center;
    font-family: "Montserrat", sans-serif; font-weight: 800;
    font-size: 118px; line-height: 1; letter-spacing: 4px;
    color: var(--red);
    text-shadow: 0 2px 0 var(--red-dark), 0 6px 10px rgba(80, 0, 0, 0.45);
  }

  .copy { position: absolute; left: 54px; top: 198px; width: 678px; }
  .copy-title {
    font-family: "Montserrat", sans-serif; font-weight: 700;
    font-size: 23px; line-height: 26px; text-transform: uppercase;
  }
  .copy p {
    font-size: 17.4px; line-height: 23.6px; text-align: justify;
    margin-bottom: 23px;
  }
  .copy-title + p { margin-top: 0; }

  .specs { position: absolute; left: 54px; top: 610px; width: 420px; }
  .specs-title {
    font-family: "Montserrat", sans-serif; font-weight: 700;
    font-size: 21px; line-height: 24px; text-transform: uppercase;
  }
  .spec-list { font-size: 15px; line-height: 20.4px; }
  .spec-row { display: flex; }
  .spec-row dt { width: 114px; }
  .spec-row dd::before { content: ": "; }

  .price {
    position: absolute; right: 57px; top: 718px;
    font-family: "Oswald", sans-serif; font-weight: 700; color: var(--red);
    text-transform: uppercase; white-space: nowrap; line-height: 1;
  }
  .price-label { font-size: 25px; font-weight: 500; }
  .price-amount { font-size: 40px; }

  .scene {
    position: absolute; left: 0; top: 840px; width: 789px; height: 276px;
    background: linear-gradient(180deg, #7ccdf0 0%, #9fe0f4 38%, var(--sea) 66%, #58d8d2 82%, var(--sand) 100%);
  }
  .palm {
    position: absolute; left: 0; top: 820px; width: 140px; height: 296px;
    background: linear-gradient(120deg, var(--leaf) 0%, rgba(63, 122, 42, 0.6) 50%, rgba(63, 122, 42, 0) 100%);
  }

  .gallery {
    position: absolute; left: 47px; top: 817px; width: 693px; height: 196px;
    background: var(--frame); padding: 10px; display: flex; gap: 9px;
  }
  .gallery-photo { height: 100%; }
  .gallery-photo.wide-a { width: 268px; background: linear-gradient(180deg, var(--cabin-light), var(--cabin)); }
  .gallery-photo.narrow { width: 118px; background: linear-gradient(180deg, #f3f3ef, #cfc7b2); }
  .gallery-photo.wide-b { width: 270px; background: linear-gradient(180deg, #e9e9e6, #d3ccba); }

  .hero-boat {
    position: absolute; left: 230px; top: 1018px; width: 430px; height: 90px;
    background: linear-gradient(180deg, rgba(255,255,255,0.85), rgba(220,228,236,0.75));
    border-radius: 40px 10px 60px 8px;
  }
</style>
</head>
<body>
  <main class="poster">
    <svg class="light-band" width="789" height="1116" viewBox="0 0 789 1116" aria-hidden="true">
      <polygon points="789,540 300,1116 789,1116" fill="var(--band-light)"/>
    </svg>

    <h1 class="headline">FOR SALE</h1>

    <section class="copy">
      <h2 class="copy-title">Speed Boat Sale</h2>
      <p>This beautiful full glass fiber speed boat (location Lombok, Indonesia) is perfect for tropical conditions. Island transfer, diving, wake boarding, fishing, private charters and leisure features.</p>
      <p>The new (2013) bought 2 x 200 HP KELTOR 4 Stroke will give you an enormous power on the water with maximum speed of 40 Knot / 74 Km/hour and will bring you within only 50 minutes from Lombok to Bali and within minute distance from all famous tropical Gili islands.</p>
      <p>The speed boat also has the comfort of a small cabin with skylight, sun controlled ventilation system, a small bed, a toilet and a fridge. In the open section of the boat are 16 seats, besides all of this is the boat equipped with brand-new GPS, Sonar and an FM / AM Radio system.</p>
      <p>This boat was built in 2011 and it was meticulously maintained to the highest standard.</p>
    </section>

    <section class="specs">
      <h2 class="specs-title">Specs :</h2>
      <dl class="spec-list">
        <div class="spec-row"><dt>Overall length</dt><dd>11 Meter 36 feet.</dd></div>
        <div class="spec-row"><dt>Built year</dt><dd>2011, Bali</dd></div>
        <div class="spec-row"><dt>Engines</dt><dd>2 x 200 HP KELTOR 4 Stroke (Bought 2013)</dd></div>
        <div class="spec-row"><dt>Capacity</dt><dd>Max. 16 People (Incl. Crew)</dd></div>
        <div class="spec-row"><dt>Max speed</dt><dd>40 Knot / 74 Km/hour</dd></div>
        <div class="spec-row"><dt>GPS / Sonar</dt><dd>Mostrel QX-52RB</dd></div>
        <div class="spec-row"><dt>Tankage</dt><dd>300 Liter</dd></div>
        <div class="spec-row"><dt>Lighting</dt><dd>LED / Halogen</dd></div>
      </dl>
    </section>

    <p class="price"><span class="price-label">Best price </span><span class="price-amount">99.000</span><span class="price-label"> USD only</span></p>

    <div class="scene" role="img" aria-label="Tropical beach with turquoise sea, rocks and palm trees"></div>
    <div class="palm" role="img" aria-label="Palm leaves at the left edge"></div>
    <div class="hero-boat" role="img" aria-label="White speed boat moored near the beach"></div>

    <div class="gallery">
      <div class="gallery-photo wide-a" role="img" aria-label="Boat interior with cream bench seats facing the helm"></div>
      <div class="gallery-photo narrow" role="img" aria-label="Small cabin bathroom with toilet"></div>
      <div class="gallery-photo wide-b" role="img" aria-label="Open deck seating with windows and captain's seat"></div>
    </div>
  </main>
</body>
</html>
```